Build PowerPoint for New Logo & Letterhead

I have started my own consulting firm and created a logo and letterhead (attached) am looking PowerPoint template. My name is Dorrit Okonkwo-Haverly and the company is called Birchpoint Consulting. We primarily use PowerPoint files to display analyses, maps and key talking points from interviews and/or recommendations. We use the documents more to facilitate discussion with our target audiences. Most of the time our PowerPoint document is printed as handouts for our clients and not projected.

Target Market(s)

Healthcare provider organizations (hospitals, health systems, physician groups)

Industry/Entity Type

Healthcare

Font styles to use
Sans Serif

Colors
abd036
1f9ad1
0355a3

Requirements
Must have
• I would like to cover page to play off of the letterhead in some fashion. I want the design to provide plenty of space for text, graphics, maps, pictures, etc.
• We will usually include our clients logo somewhere on the document. Historically it is prominent on the cover page and then in one of the corners on all of the pages thereafter.

```html
<!DOCTYPE html>
<html lang="en">
<head>
<meta charset="utf-8">
<title>Birchpoint Consulting – Presentation Template</title>
<link href="https://fonts.googleapis.com/css2?family=Open+Sans:wght@400;600;700&display=swap" rel="stylesheet">
<style>
:root{
  --green:#abd036;
  --sky:#1f9ad1;
  --navy:#0355a3;
  --ink:#333;
  --muted:#777;
  --canvas:#e9eaec;
  --line:#d6d6d6;
}
*{box-sizing:border-box;margin:0;padding:0}
html,body{width:905px;height:1200px;overflow:hidden}
body{background:var(--canvas);font-family:"Open Sans",Arial,sans-serif;color:var(--ink);position:relative}
.slide{position:absolute;width:285px;height:160px;background:#fff;overflow:hidden;box-shadow:0 1px 3px rgba(0,0,0,.18)}
.title{position:absolute;left:15px;top:12px;font-size:11px;font-weight:600;color:var(--ink)}
.badge{position:absolute;right:6px;top:4px;width:7px;height:7px;background:var(--sky);color:#fff;font-size:3px;text-align:center;line-height:7px}
.foot{position:absolute;left:0;right:0;bottom:0;height:14px}
.foot svg{position:absolute;left:0;top:0}
.foot .mark{position:absolute;left:14px;top:3px;font-size:4px;font-weight:700;color:var(--navy)}
.foot .copy{position:absolute;left:105px;top:6px;font-size:2.4px;color:var(--muted)}
.foot .client{position:absolute;right:8px;top:4px;font-size:4px;font-weight:700;color:var(--ink)}
.brand{font-weight:700;color:var(--navy);display:inline-flex;align-items:center;gap:2px}
.brand i{display:inline-block;width:5px;height:5px;background:var(--green)}
.lbl{font-size:5px;font-weight:600;color:var(--sky)}
.body{font-size:4px;line-height:1.35;color:#555}
.body li{margin-left:6px;margin-bottom:2px}
.body .sub{list-style:"– ";margin-left:12px;color:#777}
.photo{position:absolute}
.s1{background:var(--sky)}
</style>
</head>
<body>

<!-- Row 1 -->
<section class="slide s1" style="left:15px;top:18px">
  <div class="photo" role="img" aria-label="Faded photo of business people walking in a bright office lobby" style="inset:0;background:linear-gradient(160deg,#3aa8dc 0%,#1f9ad1 55%,#1788bd 100%)"></div>
  <p style="position:absolute;left:30px;right:30px;top:54px;text-align:center;color:#fff;font-size:5.5px;line-height:1.35"><b>Lorem ipsum</b> dolor sit amet, consectetur adipiscing elit. Suspendisse eget ligula mollis, mattis libero eget, rutrum ipsum.</p>
  <p style="position:absolute;left:0;right:0;top:76px;text-align:center;color:#e6f4fb;font-size:3.2px">Copyright © 2016 Birchpoint Consulting All rights reserved.</p>
  <div style="position:absolute;left:0;right:0;top:92px;text-align:center;color:#fff;font-size:7px;font-weight:700">Birchpoint</div>
</section>

<section class="slide" style="left:310px;top:18px">
  <svg width="285" height="160" style="position:absolute;left:0;top:0">
    <polyline points="0,102 165,102 180,114 285,114" fill="none" stroke="var(--green)" stroke-width="1.6"/>
    <polyline points="0,106 163,106 178,118 285,118" fill="none" stroke="var(--sky)" stroke-width="2.4"/>
    <rect x="240" y="116" width="45" height="3" fill="var(--navy)"/>
    <rect x="0" y="157" width="285" height="3" fill="var(--sky)"/>
  </svg>
  <div style="position:absolute;left:8px;top:122px;font-size:10px;font-weight:700">Presentation Title</div>
  <div style="position:absolute;left:8px;top:136px;font-size:6px">Subheading Presentation Title</div>
  <div style="position:absolute;left:8px;top:147px;font-size:3.6px">May 2016</div>
  <div class="brand" style="position:absolute;right:8px;top:138px;font-size:5px"><i></i>Birchpoint</div>
</section>

<section class="slide" style="left:606px;top:18px">
  <div style="position:absolute;left:15px;top:44px;font-size:12px;font-weight:700">Presentation Title</div>
  <div style="position:absolute;left:15px;top:62px;font-size:6.5px">Subheading Presentation Title</div>
  <div style="position:absolute;left:15px;top:77px;font-size:4px">May 2016</div>
  <svg width="285" height="160" style="position:absolute;left:0;top:0">
    <polyline points="0,120 190,120 205,110 285,110" fill="none" stroke="var(--green)" stroke-width="1.4"/>
    <polyline points="0,123 192,123 207,113 285,113" fill="none" stroke="var(--sky)" stroke-width="2"/>
    <rect x="235" y="109" width="50" height="3" fill="var(--navy)"/>
  </svg>
  <div class="brand" style="position:absolute;left:12px;top:138px;font-size:5px"><i></i>Birchpoint</div>
  <div style="position:absolute;left:52px;top:131px;font-size:3.6px;color:var(--sky);line-height:1.9">Email: dorrit@birchpointconsult.co<br>Telephone: 555.214.0387</div>
  <div style="position:absolute;right:8px;top:145px;font-size:4px;font-weight:700">client logo here</div>
</section>

<!-- Footer template reused -->
<!-- Row 2 -->
<section class="slide" style="left:15px;top:186px">
  <svg width="285" height="160" style="position:absolute;left:0;top:0">
    <polyline points="0,123 95,123 112,135 285,135" fill="none" stroke="var(--green)" stroke-width="1.4"/>
    <polyline points="0,126 97,126 114,138 285,138" fill="none" stroke="var(--sky)" stroke-width="2"/>
    <rect x="210" y="137" width="75" height="3" fill="var(--navy)"/>
    <rect x="0" y="157" width="285" height="3" fill="var(--sky)"/>
  </svg>
  <div style="position:absolute;left:8px;top:136px;font-size:9px;font-weight:700">Section Slide</div>
  <div style="position:absolute;left:8px;top:148px;font-size:5.5px">Divider Presentation Title</div>
</section>

<section class="slide" style="left:310px;top:186px">
  <div class="title">Table of Content</div><div class="badge">4</div>
  <svg width="285" height="140" style="position:absolute;left:0;top:0">
    <g fill="#fff" stroke="var(--green)" stroke-width="1">
      <circle cx="30" cy="50" r="7"/><circle cx="118" cy="50" r="7"/><circle cx="205" cy="50" r="7"/>
      <circle cx="30" cy="104" r="7"/><circle cx="118" cy="104" r="7"/><circle cx="205" cy="104" r="7"/>
    </g>
    <g font-size="6" fill="var(--sky)" text-anchor="middle" font-family="Open Sans, sans-serif">
      <text x="30" y="52">1</text><text x="118" y="52">2</text><text x="205" y="52">3</text>
      <text x="30" y="106">4</text><text x="118" y="106">5</text><text x="205" y="106">6</text>
    </g>
    <g font-size="4" font-weight="600" fill="#333" font-family="Open Sans, sans-serif">
      <text x="41" y="52">Lorem Ipsum</text><text x="129" y="52">Lorem Ipsum</text><text x="216" y="52">Lorem Ipsum</text>
      <text x="41" y="106">Lorem Ipsum</text><text x="129" y="106">Lorem Ipsum</text><text x="216" y="106">Lorem Ipsum</text>
    </g>
  </svg>
  <p class="body" style="position:absolute;left:20px;top:62px;width:72px;font-size:3.4px">Lorem ipsum dolor sit amet, te ullum corpora delicata duo. Rebum insolens pri eu. No alia tota modus qui.</p>
  <p class="body" style="position:absolute;left:108px;top:62px;width:72px;font-size:3.4px">Lorem ipsum dolor sit amet, te ullum corpora delicata duo. Rebum insolens pri eu. No alia tota modus qui.</p>
  <p class="body" style="position:absolute;left:195px;top:62px;width:72px;font-size:3.4px">Lorem ipsum dolor sit amet, te ullum corpora delicata duo. Rebum insolens pri eu. No alia tota modus qui.</p>
  <p class="body" style="position:absolute;left:20px;top:116px;width:72px;font-size:3.4px">Lorem ipsum dolor sit amet, te ullum corpora delicata duo. Rebum insolens pri eu. No alia tota modus qui.</p>
  <p class="body" style="position:absolute;left:108px;top:116px;width:72px;font-size:3.4px">Lorem ipsum dolor sit amet, te ullum corpora delicata duo. Rebum insolens pri eu. No alia tota modus qui.</p>
  <p class="body" style="position:absolute;left:195px;top:116px;width:72px;font-size:3.4px">Lorem ipsum dolor sit amet, te ullum corpora delicata duo. Rebum insolens pri eu. No alia tota modus qui.</p>
  <div class="foot"><svg width="285" height="14"><rect x="0" y="1" width="285" height="1" fill="var(--green)"/><rect x="190" y="1" width="95" height="1.5" fill="var(--navy)"/></svg><span class="mark">▪ BP</span><span class="copy">Copyright © 2016 Birchpoint Consulting All rights reserved.</span><span class="client">client logo here</span></div>
</section>

<section class="slide" style="left:606px;top:186px">
  <div class="title">One Column</div><div class="badge">5</div>
  <div class="lbl" style="position:absolute;left:15px;top:38px">Lorem Ipsum</div>
  <ul class="body" style="position:absolute;left:15px;top:46px;width:255px;font-size:3.8px">
    <li>Lorem ipsum dolor sit amet, te ullum corpora delicata duo. Rebum insolens pri eu. No alia tota modus qui.</li>
    <li class="sub">Sint brute at usu. Duo inque apparat adversarium at.</li>
    <li>Lorem ipsum dolor sit amet, te ullum corpora delicata duo. Rebum insolens pri eu. No alia tota modus qui.</li>
    <li class="sub">Sint brute at usu. Duo inque apparat adversarium at.</li>
    <li>Lorem ipsum dolor sit amet, te ullum corpora delicata duo. Rebum insolens pri eu. No alia tota modus qui.</li>
    <li class="sub">Sint brute at usu. Duo inque apparat adversarium at.</li>
    <li>Lorem ipsum dolor sit amet, te ullum corpora delicata duo. Rebum insolens pri eu. No alia tota modus qui.</li>
    <li class="sub">Sint brute at usu. Duo inque apparat adversarium at.</li>
  </ul>
  <div class="foot"><svg width="285" height="14"><rect x="0" y="1" width="285" height="1" fill="var(--green)"/><rect x="190" y="1" width="95" height="1.5" fill="var(--navy)"/></svg><span class="mark">▪ BP</span><span class="copy">Copyright © 2016 Birchpoint Consulting All rights reserved.</span><span class="client">client logo here</span></div>
</section>

<!-- Row 3 -->
<section class="slide" style="left:15px;top:354px">
  <div class="title">Two Column</div><div class="badge">6</div>
  <div class="lbl" style="position:absolute;left:15px;top:38px">Lorem Ipsum</div>
  <ul class="body" style="position:absolute;left:15px;top:46px;width:118px;font-size:3.8px">
    <li>Lorem ipsum dolor sit amet, te ullum corpora delicata duo. Rebum insolens pri eu. No alia tota modus qui.</li>
    <li class="sub">Sint brute at usu. Duo inque apparat adversarium at.</li>
    <li>Lorem ipsum dolor sit amet, te ullum corpora delicata duo. Rebum insolens pri eu. No alia tota modus qui.</li>
    <li class="sub">Sint brute at usu. Duo inque apparat adversarium at.</li>
    <li>Lorem ipsum dolor sit amet, te ullum corpora delicata duo. Rebum insolens pri eu. No alia tota modus qui.</li>
  </ul>
  <div class="lbl" style="position:absolute;left:147px;top:38px">Lorem Ipsum</div>
  <ul class="body" style="position:absolute;left:147px;top:46px;width:120px;font-size:3.8px">
    <li>Lorem ipsum dolor sit amet, te ullum corpora delicata duo. Rebum insolens pri eu. No alia tota modus qui.</li>
    <li class="sub">Sint brute at usu. Duo inque apparat adversarium at.</li>
    <li>Lorem ipsum dolor sit amet, te ullum corpora delicata duo. Rebum insolens pri eu. No alia tota modus qui.</li>
    <li class="sub">Sint brute at usu. Duo inque apparat adversarium at.</li>
    <li>Lorem ipsum dolor sit amet, te ullum corpora delicata duo. Rebum insolens pri eu. No alia tota modus qui.</li>
  </ul>
  <div class="foot"><svg width="285" height="14"><rect x="0" y="1" width="285" height="1" fill="var(--green)"/><rect x="190" y="1" width="95" height="1.5" fill="var(--navy)"/></svg><span class="mark">▪ BP</span><span class="copy">Copyright © 2016 Birchpoint Consulting All rights reserved.</span><span class="client">client logo here</span></div>
</section>

<section class="slide" style="left:310px;top:354px">
  <div class="title">Left Column</div><div class="badge">7</div>
  <div class="lbl" style="position:absolute;left:15px;top:38px">Lorem Ipsum</div>
  <ul class="body" style="position:absolute;left:15px;top:46px;width:118px;font-size:3.8px">
    <li>Lorem ipsum dolor sit amet, te ullum corpora delicata duo. Rebum insolens pri eu. No alia tota modus qui.</li>
    <li class="sub">Sint brute at usu. Duo inque apparat adversarium at.</li>
    <li>Lorem ipsum dolor sit amet, te ullum corpora delicata duo. Rebum insolens pri eu. No alia tota modus qui.</li>
    <li class="sub">Sint brute at usu. Duo inque apparat adversarium at.</li>
    <li>Lorem ipsum dolor sit amet, te ullum corpora delicata duo. Rebum insolens pri eu. No alia tota modus qui.</li>
  </ul>
  <svg width="285" height="160" style="position:absolute;left:0;top:0">
    <polygon points="210,40 198,58 222,58" fill="#ddd"/>
    <polygon points="197,60 223,60 235,78 185,78" fill="var(--navy)"/>
    <polygon points="184,80 236,80 248,98 172,98" fill="var(--sky)"/>
    <polygon points="171,100 249,100 261,120 159,120" fill="var(--green)"/>
  </svg>
  <div class="foot"><svg width="285" height="14"><rect x="0" y="1" width="285" height="1" fill="var(--green)"/><rect x="190" y="1" width="95" height="1.5" fill="var(--navy)"/></svg><span class="mark">▪ BP</span><span class="copy">Copyright © 2016 Birchpoint Consulting All rights reserved.</span><span class="client">client logo here</span></div>
</section>

<section class="slide" style="left:606px;top:354px">
  <div class="photo" role="img" aria-label="Photo of a smiling doctor in a white coat with a stethoscope" style="left:0;top:0;width:140px;height:146px;background:linear-gradient(135deg,#f3f5f7,#dfe6ec 60%,#c9d3dc)"></div>
  <div class="title" style="left:148px">Right Column With Image</div><div class="badge">8</div>
  <div class="lbl" style="position:absolute;left:150px;top:38px">Lorem Ipsum</div>
  <ul class="body" style="position:absolute;left:150px;top:46px;width:122px;font-size:3.8px">
    <li>Lorem ipsum dolor sit amet, te ullum corpora delicata duo. Rebum insolens pri eu. No alia tota modus qui.</li>
    <li class="sub">Sint brute at usu. Duo inque apparat adversarium at.</li>
    <li>Lorem ipsum dolor sit amet, te ullum corpora delicata duo. Rebum insolens pri eu. No alia tota modus qui.</li>
    <li class="sub">Sint brute at usu. Duo inque apparat adversarium at.</li>
    <li>Lorem ipsum dolor sit amet, te ullum corpora delicata duo. Rebum insolens pri eu. No alia tota modus qui.</li>
  </ul>
  <div class="foot"><svg width="285" height="14"><rect x="0" y="1" width="285" height="1" fill="var(--green)"/><rect x="190" y="1" width="95" height="1.5" fill="var(--navy)"/></svg><span class="mark">▪ BP</span><span class="copy">Copyright © 2016 Birchpoint Consulting All rights reserved.</span><span class="client">client logo here</span></div>
</section>

<!-- Row 4 -->
<section class="slide" style="left:15px;top:522px">
  <div class="title">Our Team</div><div class="badge">9</div>
  <svg width="285" height="160" style="position:absolute;left:0;top:0" font-family="Open Sans, sans-serif">
    <g fill="#e4e9ee" stroke="var(--green)" stroke-width="1">
      <circle cx="59" cy="52" r="17"/><circle cx="144" cy="52" r="17"/><circle cx="229" cy="52" r="17"/>
      <circle cx="59" cy="110" r="17"/><circle cx="144" cy="110" r="17"/><circle cx="229" cy="110" r="17"/>
    </g>
    <g font-size="4.4" font-weight="600" fill="var(--sky)" text-anchor="middle" font-style="normal">
      <text x="59" y="77">Sam Rivera</text><text x="144" y="77">Sam Rivera</text><text x="229" y="77">Sam Rivera</text>
      <text x="59" y="135">Sam Rivera</text><text x="144" y="135">Sam Rivera</text><text x="229" y="135">Sam Rivera</text>
    </g>
    <g font-size="3.4" fill="#888" text-anchor="middle">
      <text x="59" y="82">Doctor</text><text x="144" y="82">Doctor</text><text x="229" y="82">Doctor</text>
      <text x="59" y="140">Doctor</text><text x="144" y="140">Doctor</text><text x="229" y="140">Doctor</text>
    </g>
  </svg>
  <div class="foot"><svg width="285" height="14"><rect x="0" y="1" width="285" height="1" fill="var(--green)"/><rect x="190" y="1" width="95" height="1.5" fill="var(--navy)"/></svg><span class="mark">▪ BP</span><span class="copy">Copyright © 2016 Birchpoint Consulting All rights reserved.</span><span class="client">client logo here</span></div>
</section>

<section class="slide" style="left:310px;top:522px">
  <div class="title">Table Sample</div><div class="badge">10</div>
  <svg width="285" height="160" style="position:absolute;left:0;top:0" font-family="Open Sans, sans-serif">
    <rect x="15" y="36" width="63" height="10" fill="var(--green)"/>
    <rect x="78" y="36" width="68" height="10" fill="var(--sky)"/>
    <rect x="146" y="36" width="68" height="10" fill="var(--navy)"/>
    <rect x="214" y="36" width="58" height="10" fill="#999"/>
    <g font-size="4" font-weight="600" fill="#fff" text-anchor="middle">
      <text x="46" y="43">Lorem ipsum</text><text x="112" y="43">Lorem ipsum 1</text><text x="180" y="43">Lorem ipsum 2</text><text x="243" y="43">Lorem ipsum 3</text>
    </g>
    <rect x="15" y="46" width="257" height="18" fill="#f1f1f1"/>
    <rect x="15" y="82" width="257" height="16" fill="#f1f1f1"/>
    <rect x="15" y="98" width="257" height="16" fill="#e4e4e4"/>
    <g fill="#bbb">
      <rect x="19" y="50" width="50" height="1.5"/><rect x="82" y="50" width="55" height="1.5"/><rect x="150" y="50" width="55" height="1.5"/><rect x="218" y="50" width="48" height="1.5"/>
      <rect x="19" y="54" width="40" height="1.5"/><rect x="82" y="54" width="45" height="1.5"/><rect x="150" y="54" width="45" height="1.5"/><rect x="218" y="54" width="40" height="1.5"/>
      <rect x="19" y="69" width="50" height="1.5"/><rect x="82" y="69" width="55" height="1.5"/><rect x="150" y="69" width="55" height="1.5"/><rect x="218" y="69" width="48" height="1.5"/>
      <rect x="19" y="87" width="50" height="1.5"/><rect x="82" y="87" width="55" height="1.5"/><rect x="150" y="87" width="55" height="1.5"/><rect x="218" y="87" width="48" height="1.5"/>
      <rect x="19" y="103" width="50" height="1.5"/><rect x="82" y="103" width="55" height="1.5"/><rect x="150" y="103" width="55" height="1.5"/><rect x="218" y="103" width="48" height="1.5"/>
      <rect x="19" y="119" width="50" height="1.5"/><rect x="82" y="119" width="55" height="1.5"/><rect x="150" y="119" width="55" height="1.5"/><rect x="218" y="119" width="48" height="1.5"/>
    </g>
  </svg>
  <div class="foot"><svg width="285" height="14"><rect x="0" y="1" width="285" height="1" fill="var(--green)"/><rect x="190" y="1" width="95" height="1.5" fill="var(--navy)"/></svg><span class="mark">▪ BP</span><span class="copy">Copyright © 2016 Birchpoint Consulting All rights reserved.</span><span class="client">client logo here</span></div>
</section>

<section class="slide" style="left:606px;top:522px">
  <div class="title">About Us</div><div class="badge">11</div>
  <div class="photo" role="img" aria-label="Round portrait photo of a doctor" style="left:14px;top:40px;width:90px;height:90px;border-radius:50%;background:radial-gradient(circle at 50% 45%,#eef1f4,#cfd8e0)"></div>
  <div class="lbl" style="position:absolute;left:116px;top:40px">Lorem Ipsum is simply dummy</div>
  <p class="body" style="position:absolute;left:116px;top:50px;width:158px;font-size:3.5px">Text of the printing and typesetting industry. Lorem Ipsum has been the industry's standard dummy text ever since the 1500s, when an unknown printer took a galley of type and scrambled it to make a type specimen book. It has survived not only five centuries, but also the leap into electronic typesetting, remaining essentially unchanged. It was popularised in the 1960s with the release of sheets containing Lorem Ipsum passages, and more recently with desktop publishing software. Lorem Ipsum has been the industry's standard dummy text ever since the 1500s, when an unknown printer took a galley of type and scrambled.</p>
  <div class="foot"><svg width="285" height="14"><rect x="0" y="1" width="285" height="1" fill="var(--green)"/><rect x="190" y="1" width="95" height="1.5" fill="var(--navy)"/></svg><span class="mark">▪ BP</span><span class="copy">Copyright © 2016 Birchpoint Consulting All rights reserved.</span><span class="client">client logo here</span></div>
</section>

<!-- Row 5 -->
<section class="slide" style="left:15px;top:690px">
  <div class="title">Pie Chart Sample</div><div class="badge">12</div>
  <div style="position:absolute;left:0;right:0;top:32px;text-align:center;font-size:6px;font-weight:600">Lorem ipsum dolar sit amet</div>
  <div role="img" aria-label="Pie chart: 58%, 23%, 10%, 5%" style="position:absolute;left:103px;top:52px;width:66px;height:66px;border-radius:50%;background:conic-gradient(var(--green) 0 58%,var(--sky) 58% 81%,var(--navy) 81% 91%,#e2e2e2 91% 100%)"></div>
  <div style="position:absolute;left:150px;top:81px;font-size:4px;color:#fff">58%</div>
  <div style="position:absolute;left:112px;top:94px;font-size:4px;color:#fff">23%</div>
  <div style="position:absolute;left:115px;top:76px;font-size:4px;color:#fff">10%</div>
  <div style="position:absolute;left:130px;top:58px;font-size:4px;color:#888">5%</div>
  <div style="position:absolute;left:0;right:0;top:133px;text-align:center;font-size:3.2px;color:#777;word-spacing:2px">● Lorem ipsum &nbsp; ● Lorem ipsum &nbsp; ● Lorem ipsum &nbsp; ● Lorem ipsum</div>
  <div class="foot"><svg width="285" height="14"><rect x="0" y="1" width="285" height="1" fill="var(--green)"/><rect x="190" y="1" width="95" height="1.5" fill="var(--navy)"/></svg><span class="mark">▪ BP</span><span class="copy">Copyright © 2016 Birchpoint Consulting All rights reserved.</span><span class="client">client logo here</span></div>
</section>

<section class="slide" style="left:310px;top:690px">
  <div class="title">Basic Chevron Process</div><div class="badge">13</div>
  <svg width="285" height="160" style="position:absolute;left:0;top:0" font-family="Open Sans, sans-serif">
    <polygon points="20,36 98,36 106,52 98,68 20,68" fill="var(--green)"/>
    <polygon points="101,36 180,36 188,52 180,68 101,68 109,52" fill="var(--sky)"/>
    <polygon points="183,36 264,36 272,52 264,68 183,68 191,52" fill="var(--navy)"/>
    <g font-size="6" fill="#fff" text-anchor="middle"><text x="62" y="54">Lorem ipsum</text><text x="142" y="54">Lorem ipsum</text><text x="224" y="54">Lorem ipsum</text></g>
  </svg>
  <ul class="body" style="position:absolute;left:22px;top:78px;width:70px;font-size:3.6px"><li>Lorem ipsum dolor sit amet, consectetur adipiscing elit</li><li>Nunc quis dui dolor</li><li>Maecenas sem nibh, congue a urna non, volutpat porttitor justo</li></ul>
  <ul class="body" style="position:absolute;left:104px;top:78px;width:70px;font-size:3.6px"><li>Lorem ipsum dolor sit amet, consectetur adipiscing elit</li><li>Nunc quis dui dolor</li><li>Maecenas sem nibh, congue a urna non, volutpat porttitor justo</li></ul>
  <ul class="body" style="position:absolute;left:186px;top:78px;width:72px;font-size:3.6px"><li>Lorem ipsum dolor sit amet, consectetur adipiscing elit</li><li>Nunc quis dui dolor</li><li>Maecenas sem nibh, congue a urna non, volutpat porttitor justo</li></ul>
  <div class="foot"><svg width="285" height="14"><rect x="0" y="1" width="285" height="1" fill="var(--green)"/><rect x="190" y="1" width="95" height="1.5" fill="var(--navy)"/></svg><span class="mark">▪ BP</span><span class="copy">Copyright © 2016 Birchpoint Consulting All rights reserved.</span><span class="client">client logo here</span></div>
</section>

<section class="slide" style="left:606px;top:690px">
  <div class="title">Linier VEEN</div><div class="badge">14</div>
  <svg width="285" height="160" style="position:absolute;left:0;top:0">
    <circle cx="70" cy="87" r="40" fill="var(--green)" opacity=".9"/>
    <circle cx="144" cy="87" r="40" fill="var(--sky)" opacity=".85"/>
    <circle cx="216" cy="87" r="40" fill="var(--navy)" opacity=".8"/>
  </svg>
  <p class="body" style="position:absolute;left:44px;top:68px;width:52px;text-align:center;color:#fff;font-size:3.4px">Lorem ipsum dolor sit amet, consectetur adipiscing elit. Nunc quis dui dolor. Maecenas sem nibh, congue a urna non, volutpat porttitor justo.</p>
  <p class="body" style="position:absolute;left:118px;top:68px;width:52px;text-align:center;color:#fff;font-size:3.4px">Lorem ipsum dolor sit amet, consectetur adipiscing elit. Nunc quis dui dolor. Maecenas sem nibh, congue a urna non, volutpat porttitor justo.</p>
  <p class="body" style="position:absolute;left:190px;top:68px;width:52px;text-align:center;color:#fff;font-size:3.4px">Lorem ipsum dolor sit amet, consectetur adipiscing elit. Nunc quis dui dolor. Maecenas sem nibh, congue a urna non, volutpat porttitor justo.</p>
  <div class="foot"><svg width="285" height="14"><rect x="0" y="1" width="285" height="1" fill="var(--green)"/><rect x="190" y="1" width="95" height="1.5" fill="var(--navy)"/></svg><span class="mark">▪ BP</span><span class="copy">Copyright © 2016 Birchpoint Consulting All rights reserved.</span><span class="client">client logo here</span></div>
</section>

<!-- Row 6 -->
<section class="slide" style="left:15px;top:858px">
  <div class="title">Bar Chart Sample</div><div class="badge">15</div>
  <div style="position:absolute;left:0;right:0;top:32px;text-align:center;font-size:6px;font-weight:600">Lorem ipsum dolor sit amet</div>
  <svg width="285" height="160" style="position:absolute;left:0;top:0" font-family="Open Sans, sans-serif">
    <g stroke="#eee" stroke-width=".5"><line x1="30" y1="52" x2="270" y2="52"/><line x1="30" y1="65" x2="270" y2="65"/><line x1="30" y1="78" x2="270" y2="78"/><line x1="30" y1="91" x2="270" y2="91"/><line x1="30" y1="104" x2="270" y2="104"/><line x1="30" y1="117" x2="270" y2="117"/></g>
    <line x1="30" y1="130" x2="270" y2="130" stroke="#ccc" stroke-width=".6"/>
    <rect x="40" y="68" width="9" height="62" fill="var(--green)"/>
    <rect x="63" y="96" width="9" height="34" fill="var(--green)"/>
    <rect x="86" y="83" width="9" height="47" fill="var(--green)"/>
    <rect x="109" y="67" width="9" height="63" fill="var(--sky)"/>
    <rect x="132" y="103" width="9" height="27" fill="var(--sky)"/>
    <rect x="155" y="110" width="9" height="20" fill="var(--sky)"/>
    <rect x="178" y="54" width="9" height="76" fill="var(--navy)"/>
    <rect x="201" y="90" width="9" height="40" fill="var(--navy)"/>
    <rect x="224" y="98" width="9" height="32" fill="var(--navy)"/>
    <rect x="247" y="74" width="9" height="56" fill="#999"/>
    <g font-size="2.8" fill="#888" text-anchor="middle">
      <text x="44" y="136">Category 1</text><text x="67" y="136">Category 2</text><text x="90" y="136">Category 3</text><text x="113" y="136">Category 4</text><text x="136" y="136">Category 5</text><text x="159" y="136">Category 6</text><text x="182" y="136">Category 7</text><text x="205" y="136">Category 8</text><text x="228" y="136">Category 9</text><text x="251" y="136">Category 10</text>
    </g>
  </svg>
  <div class="foot"><svg width="285" height="14"><rect x="0" y="1" width="285" height="1" fill="var(--green)"/><rect x="190" y="1" width="95" height="1.5" fill="var(--navy)"/></svg><span class="mark">▪ BP</span><span class="copy">Copyright © 2016 Birchpoint Consulting All rights reserved.</span><span class="client">client logo here</span></div>
</section>

<section class="slide" style="left:310px;top:858px">
  <div class="title">Graphic Sample</div><div class="badge">16</div>
  <svg width="285" height="160" style="position:absolute;left:0;top:0" font-family="Open Sans, sans-serif">
    <circle cx="142" cy="84" r="28" fill="none" stroke="#ddd" stroke-width="1.2"/>
    <g fill="#fff" stroke="var(--green)" stroke-width=".8">
      <circle cx="142" cy="56" r="6"/><circle cx="166" cy="70" r="6"/><circle cx="166" cy="98" r="6"/>
      <circle cx="142" cy="112" r="6"/><circle cx="118" cy="98" r="6"/><circle cx="118" cy="70" r="6"/>
    </g>
    <g fill="none" stroke="var(--sky)" stroke-width=".7">
      <circle cx="142" cy="56" r="2"/><path d="M164 68h4v4h-4z"/><path d="M164 98h4M166 96v4"/>
      <path d="M140 112l1.5 1.5 3-3"/><circle cx="118" cy="98" r="2"/><path d="M116 70h4M116 72h4"/>
    </g>
    <text x="142" y="87" text-anchor="middle" font-size="6" font-weight="700" fill="#0355a3">Birchpoint</text>
  </svg>
  <p class="body" style="position:absolute;left:112px;top:28px;width:60px;text-align:center;font-size:3.4px">Lorem ipsum dolor sit amet, consectetur adipiscing elit</p>
  <p class="body" style="position:absolute;left:40px;top:58px;width:72px;text-align:center;font-size:3.4px">Lorem ipsum dolor sit amet, consectetur adipiscing elit</p>
  <p class="body" style="position:absolute;left:178px;top:58px;width:72px;text-align:center;font-size:3.4px">Lorem ipsum dolor sit amet, consectetur adipiscing elit</p>
  <p class="body" style="position:absolute;left:40px;top:100px;width:72px;text-align:center;font-size:3.4px">Lorem ipsum dolor sit amet, consectetur adipiscing elit</p>
  <p class="body" style="position:absolute;left:178px;top:100px;width:72px;text-align:center;font-size:3.4px">Lorem ipsum dolor sit amet, consectetur adipiscing elit</p>
  <p class="body" style="position:absolute;left:112px;top:128px;width:60px;text-align:center;font-size:3.4px">Lorem ipsum dolor sit amet, consectetur adipiscing elit</p>
  <div class="foot"><svg width="285" height="14"><rect x="0" y="1" width="285" height="1" fill="var(--green)"/><rect x="190" y="1" width="95" height="1.5" fill="var(--navy)"/></svg><span class="mark">▪ BP</span><span class="copy">Copyright © 2016 Birchpoint Consulting All rights reserved.</span><span class="client">client logo here</span></div>
</section>

<section class="slide" style="left:606px;top:858px">
  <div class="photo" role="img" aria-label="Photo of smiling medical team members in conversation" style="left:0;top:0;width:285px;height:95px;background:linear-gradient(120deg,#9aa4ad,#c7ced4 45%,#7f8a94)"></div>
  <div class="title" style="color:#fff">Content With Icon Sample</div>
  <svg width="285" height="160" style="position:absolute;left:0;top:0">
    <g stroke="#fff" stroke-width="1.2">
      <circle cx="46" cy="94" r="8" fill="var(--green)"/><circle cx="110" cy="94" r="8" fill="var(--sky)"/><circle cx="175" cy="94" r="8" fill="var(--navy)"/><circle cx="240" cy="94" r="8" fill="#999"/>
    </g>
    <g fill="none" stroke="#fff" stroke-width=".9">
      <circle cx="45" cy="93" r="3"/><path d="M47 95l3 3"/>
      <rect x="106" y="90" width="8" height="6"/><path d="M110 96v2M108 98h4"/>
      <circle cx="175" cy="94" r="3.5"/><circle cx="175" cy="94" r="1.2"/>
      <path d="M236 98l8-8M236 90l8 8"/>
    </g>
  </svg>
  <div style="position:absolute;top:106px;left:0;width:285px;display:flex;justify-content:space-around;padding:0 12px">
    <div style="width:52px;text-align:center"><div class="lbl" style="color:var(--green)">Lorem ipsum</div><p class="body" style="font-size:3.2px">Lorem ipsum dolor sit amet, consectetur adipiscing elit</p></div>
    <div style="width:52px;text-align:center"><div class="lbl">Lorem ipsum</div><p class="body" style="font-size:3.2px">Lorem ipsum dolor sit amet, consectetur adipiscing elit</p></div>
    <div style="width:52px;text-align:center"><div class="lbl" style="color:var(--navy)">Lorem ipsum</div><p class="body" style="font-size:3.2px">Lorem ipsum dolor sit amet, consectetur adipiscing elit</p></div>
    <div style="width:52px;text-align:center"><div class="lbl" style="color:#888">Lorem ipsum</div><p class="body" style="font-size:3.2px">Lorem ipsum dolor sit amet, consectetur adipiscing elit</p></div>
  </div>
  <div class="foot"><svg width="285" height="14"><rect x="0" y="1" width="285" height="1" fill="var(--green)"/><rect x="190" y="1" width="95" height="1.5" fill="var(--navy)"/></svg><span class="mark">▪ BP</span><span class="copy">Copyright © 2016 Birchpoint Consulting All rights reserved.</span><span class="client">client logo here</span></div>
</section>

<!-- Row 7 -->
<section class="slide" style="left:177px;top:1026px">
  <div class="photo" role="img" aria-label="Darkened photo of a doctor consulting with a patient" style="inset:0;background:linear-gradient(120deg,#4d5660,#6e7780 50%,#3f4850)"></div>
  <div style="position:absolute;left:0;right:0;top:13px;text-align:center;color:#fff;font-size:10px;font-weight:600">Testimonials</div>
  <svg width="285" height="160" style="position:absolute;left:0;top:0"><circle cx="142" cy="60" r="10" fill="var(--green)"/><text x="142" y="66" text-anchor="middle" font-size="14" font-weight="700" fill="#fff" font-family="Open Sans, sans-serif">“</text></svg>
  <p style="position:absolute;left:20px;right:20px;top:80px;text-align:center;color:#fff;font-size:5px;line-height:1.4">Lorem Ipsum is simply dummy text of the printing and typesetting industry. Lorem Ipsum has been the industry's standard dummy text ever since the 1500s, when an unknown printer took a galley of type and scrambled it to make a type specimen book.</p>
  <div style="position:absolute;left:0;right:0;top:112px;text-align:center;color:#fff;font-size:5px;font-weight:700">- Sam Rivera -</div>
</section>

<section class="slide" style="left:472px;top:1026px">
  <svg width="285" height="160" style="position:absolute;left:0;top:0">
    <polygon points="0,0 285,0 285,18 160,18 148,28 0,28" fill="var(--sky)"/>
    <polygon points="0,28 148,28 144,31 0,31" fill="var(--green)"/>
    <polygon points="0,140 120,140 132,130 285,130 285,160 0,160" fill="var(--green)"/>
    <rect x="132" y="128" width="153" height="2.5" fill="var(--navy)"/>
  </svg>
  <div style="position:absolute;left:8px;top:44px;font-size:8px;font-weight:700">THANK YOU FONT 24PT</div>
  <div style="position:absolute;left:8px;top:60px;font-size:3.6px;line-height:1.4;color:#555">
    <b style="color:#333">ADDRESS</b><br>Lorem ipsum<br>
    <b style="color:#333">PHONE/FAX</b><br>Call 555-300-0000<br>Fax 555-300-0001<br>
    <b style="color:#333">EMAIL</b><br>loremipsum@example.com<br>
    <b style="color:#333">WEBSITE</b><br>www.example.com
  </div>
  <div class="brand" style="position:absolute;left:214px;top:56px;font-size:7px"><i style="width:7px;height:7px"></i>Birchpoint</div>
  <p class="body" style="position:absolute;left:180px;top:78px;width:95px;text-align:center;font-size:3.4px">Lorem Ipsum is simply dummy text of the printing and typesetting industry. Lorem Ipsum has been the industry's standard dummy text ever since the 1500s, when an unknown printer took a galley of type and scrambled it to make a type specimen.</p>
</section>

</body>
</html>
```